Design the Marketing Brochure for a service company with Zenith 500 Clients

We need to redesign our marketing brochures to reflect the new service lines we have added in the last few years. We are a professional staffing firm based in Miami, Florida and have a portfolio of clients that include: Velmora Seaways, Tidewell Voyage Lines, Grillano Foods Corp, Horizon Lens Network Etc. I have attached our current marketing inserts in pdf format. I would like to have 5 inserts displaying our services, process and business lines.

Target Market(s)

Zenith 1000 companies. Within those companies our clients are: CFO's, VP of Finance, Controller, Head of Human Resources, Banking Executives etc. All financial related roles.

Industry/Entity Type

Recruitment

Colors
ec1f27
ffffff
aaaaaa
fece3e
000000

Requirements
Must have
• 5 pages 3 of which we have mots of the content. One page dedicated to " Temporary Staffing" and one page dedicated to our "Banking Division" The brochures should include professional pictures and a well designed layout that looks professional and appealing to an educated client. Our colors are Red, Gray and White.
• Please see our attached brochures and our website at www.kvtrecruit.example
Nice to have
• Professional pictures of people in the business workplace.
Should not have
• Graphics or cartoons of any kind.

```html
<!DOCTYPE html>
<html lang="en">
<head>
<meta charset="utf-8">
<title>KVT International – Overview Insert</title>
<link rel="stylesheet" href="https://fonts.googleapis.com/css2?family=Libre+Baskerville:wght@700&family=Roboto:wght@300;400;700&family=Lato:wght@300;400&display=swap">
<style>
  :root {
    --brand-red: #8e0b0b;
    --heading-red: #9a0d0d;
    --text-gray: #777;
    --panel-gray: #e2e2e2;
    --charcoal: #444;
    --backdrop: #b3b3b3;
    --white: #fff;
  }
  * { box-sizing: border-box; margin: 0; padding: 0; }
  html, body { width: 1200px; height: 1200px; overflow: hidden; background: var(--backdrop); }
  .sheet {
    position: absolute; left: 176px; top: 0; width: 848px; height: 1200px;
    background: var(--white); font-family: "Roboto", Arial, sans-serif; overflow: hidden;
  }
  .masthead { position: absolute; left: 0; top: 0; width: 100%; height: 119px; display: flex; justify-content: center; align-items: center; }
  .brand-name { font-family: "Roboto", Arial, sans-serif; font-weight: 400; font-size: 30px; color: var(--brand-red); letter-spacing: 1px; }
  .band { position: absolute; left: 0; width: 100%; background: var(--brand-red); }
  .band.top { top: 119px; height: 14px; }
  .band.mid { top: 616px; height: 15px; }
  .hero-photo {
    position: absolute; left: 0; top: 133px; width: 100%; height: 483px;
    background: linear-gradient(180deg, #bdb89c 0%, #d8d6c2 35%, #c9cdbf 60%, #a9aba2 100%);
  }
  .section-tab {
    position: absolute; left: 37px; top: 604px; width: 229px; height: 81px; background: var(--charcoal);
    color: var(--white); font-family: "Libre Baskerville", Georgia, serif; font-size: 28px; font-weight: 700;
    display: flex; align-items: center; padding-left: 23px;
  }
  .main-col { position: absolute; left: 41px; top: 705px; width: 474px; color: var(--text-gray); font-weight: 300; font-size: 11.6px; line-height: 14.4px; }
  .main-col p { text-align: justify; }
  .sub-heading { color: var(--heading-red); font-weight: 700; font-size: 21px; letter-spacing: -0.3px; margin: 10px 0 9px -3px; }
  .objectives { list-style: none; margin-top: 11px; }
  .objectives > li { position: relative; padding-left: 15px; margin-bottom: 14px; }
  .objectives > li::before { content: "✖"; position: absolute; left: 0; top: 0; color: var(--heading-red); font-size: 10px; }
  .steps { list-style: none; margin-top: 13px; padding-left: 9px; }
  .steps li { position: relative; padding-left: 11px; margin-bottom: 6px; }
  .steps li::before { content: "›"; position: absolute; left: 0; top: -2px; color: #222; font-weight: 700; font-size: 15px; }
  .guarantee-panel { position: absolute; left: 527px; top: 631px; width: 321px; height: 306px; background: var(--panel-gray); padding: 28px 30px 0 14px; }
  .guarantee-panel h2 { color: var(--heading-red); font-weight: 700; font-size: 21px; letter-spacing: -0.3px; margin-bottom: 15px; }
  .guarantee-panel p { color: #555; font-weight: 400; font-size: 11.3px; line-height: 14.4px; text-align: justify; }
  .panel-rule { position: absolute; left: 525px; top: 937px; width: 323px; height: 7px; background: var(--charcoal); }
  .desk-photo { position: absolute; left: 527px; top: 944px; width: 321px; height: 198px; background: linear-gradient(135deg, #8a8a88 0%, #cfcfcf 45%, #efefef 75%, #bdbdbd 100%); }
  .contact-bar { position: absolute; left: 0; top: 1142px; width: 100%; height: 58px; background: var(--brand-red); color: var(--white); font-family: "Lato", Arial, sans-serif; font-weight: 300; font-size: 14px; }
  .contact-bar span { position: absolute; top: 22px; }
  .contact-divider { position: absolute; top: 8px; width: 2px; height: 43px; background: var(--white); }
</style>
</head>
<body>
<div class="sheet">
  <header class="masthead">
    <div class="brand-name">KVT International</div>
  </header>
  <div class="band top"></div>
  <div class="hero-photo" role="img" aria-label="Businessman on a ladder looking through binoculars over a misty landscape"></div>
  <div class="band mid"></div>
  <div class="section-tab">OVERVIEW</div>

  <section class="main-col">
    <p>KVT International is a specialized professional recruitment firm built with a global economy in mind. We provide customized human capital solutions including Executive Recruitment, Direct Hire and Temporary Staffing, to both domestic and international organizations from our headquarters in Miami, Florida. Our functional areas of expertise include Accounting, Finance and Human Resources</p>
    <h2 class="sub-heading">OUR VISION</h2>
    <p>KVT International was founded with a vision intended to successfully achieve the following objectives:</p>
    <ul class="objectives">
      <li>Creating value for our clients by reaching multi-cultural and bilingual talent, which is the key component in their ability to expand into Latin America and other international markets</li>
      <li>Providing a seamless recruitment process from beginning to end by:
        <ul class="steps">
          <li>Providing excellent research capabilities and access to a global talent pool</li>
          <li>Performing an extensive organizational and cultural assessment</li>
          <li>In depth reference checking</li>
          <li>Critical contribution to the successful completion of the search by fully participating in the final negotiations</li>
        </ul>
      </li>
      <li>Creating a connection with our applicants by becoming their trusted advisor and a resource for top employment opportunities throughout their career</li>
    </ul>
  </section>

  <aside class="guarantee-panel">
    <h2>120% GUARANTEE</h2>
    <p>When you hire a temporary employee or contractor through KVT International, we guarantee a positive experience. Since we are a firm that strives to build long term relationships with our clients, we decided a long time ago that 100% satisfaction guarantee wasn't good enough. We're so confident in our ability to deliver high quality temporary employees that we offer the KVT International 120% Guarantee. If you are ever dissatisfied with the performance of a KVT International temporary employee, reach out to us right away. You will then receive a 100% credit for the first day of work, plus a 20% discount for the first day of the replacement we send over. At KVT International, we are not satisfied until you are</p>
  </aside>
  <div class="panel-rule"></div>
  <div class="desk-photo" role="img" aria-label="Hands using a computer mouse and laptop keyboard at a desk"></div>

  <footer class="contact-bar">
    <span style="left:38px">4410 NW 22 Court, Suite 215 Doral, FL 33166</span>
    <div class="contact-divider" style="left:358px"></div>
    <span style="left:392px">Office: 786.555-0KVT</span>
    <div class="contact-divider" style="left:554px"></div>
    <span style="left:588px">Email: info@kvtrecruit.example</span>
  </footer>
</div>
</body>
</html>
```